KPT Building And Maintenance

Need a very professional looking double sided Buisiness card with all my details phone number, name, email, license number.

Target Market(s)

construction industry

Industry/Entity Type

building

Contact Information for Business Card

Name Dale Whitcombe. Email Address Info@KPTBuilding.example.au mobile number 0452918730 licence number 871406D. web site

```html
<!DOCTYPE html>
<html lang="en">
<head>
<meta charset="utf-8">
<title>KPT Building And Maintenance – Business Card</title>
<link rel="stylesheet" href="https://fonts.googleapis.com/css2?family=Open+Sans:wght@400;600;700&display=swap">
<style>
  :root {
    --backdrop: #d3d3d3;
    --card-white: #ffffff;
    --card-dark: #262626;
    --brand-blue: #3d96d8;
    --ink: #3a3a3a;
    --rule: #6b6b6b;
    --light-text: #ffffff;
  }
  * { margin: 0; padding: 0; box-sizing: border-box; }
  html, body {
    width: 1200px; height: 788px; overflow: hidden;
    background: var(--backdrop);
    font-family: "Open Sans", sans-serif;
  }
  .sheet {
    position: relative; width: 1200px; height: 788px;
    display: flex; align-items: center; justify-content: center; gap: 40px;
  }
  .card {
    position: relative; width: 550px; height: 314px;
    border-radius: 22px; overflow: hidden;
    box-shadow: 0 10px 24px rgba(0,0,0,0.18);
  }
  .card--front { background: var(--card-white); }
  .card--back { background: var(--card-dark); }

  .front-wedge { position: absolute; inset: 0; width: 550px; height: 314px; }

  .brand-name {
    position: absolute; display: flex; align-items: center; gap: 10px;
    font-weight: 700; text-transform: uppercase; letter-spacing: 1px; line-height: 1;
    white-space: nowrap;
  }
  .brand-name__mark { display: block; flex: none; background: var(--brand-blue); }
  .card--front .brand-name { left: 40px; top: 58px; font-size: 32px; color: var(--ink); }
  .card--front .brand-name__mark { width: 22px; height: 22px; }
  .card--back .brand-name {
    left: 50%; top: 50%; transform: translate(-50%, -50%);
    font-size: 44px; color: var(--light-text);
  }
  .card--back .brand-name__mark { width: 30px; height: 30px; }

  .holder { position: absolute; right: 130px; top: 128px; text-align: right; white-space: nowrap; }
  .holder__name {
    font-size: 22px; font-weight: 600; color: var(--brand-blue);
    text-transform: uppercase; letter-spacing: 0.5px; line-height: 1.1;
  }
  .holder__role { font-size: 12px; color: var(--ink); margin-top: 2px; }

  .divider {
    position: absolute; left: 34px; top: 196px; width: 360px; height: 1px;
    background: var(--rule);
  }

  .contact-list { position: absolute; left: 44px; top: 212px; list-style: none; }
  .contact-list li {
    display: flex; align-items: center; gap: 8px;
    font-size: 14px; color: var(--ink); line-height: 24px; white-space: nowrap;
  }
  .contact-list svg { width: 11px; height: 11px; flex: none; }

  .licence {
    position: absolute; right: 26px; bottom: 18px;
    font-size: 12px; color: var(--light-text); letter-spacing: 0.3px; white-space: nowrap;
  }
</style>
</head>
<body>
<main class="sheet">
  <section class="card card--front" aria-label="Business card front">
    <svg class="front-wedge" viewBox="0 0 550 314" aria-hidden="true">
      <polygon points="530,62 550,62 550,68 322,314 300,314" fill="var(--brand-blue)"/>
      <polygon points="550,80 550,314 330,314" fill="var(--card-dark)"/>
    </svg>

    <div class="brand-name"><span class="brand-name__mark"></span>KPT Building</div>

    <div class="holder">
      <p class="holder__name">Dale Whitcombe</p>
      <p class="holder__role">Managing Director</p>
    </div>

    <div class="divider"></div>

    <ul class="contact-list">
      <li>
        <svg viewBox="0 0 12 12"><path d="M3 1 L5 3.5 L4 5 Q5 7 7 8 L8.5 7 L11 9 L9.5 11 Q4 10.5 1 3 Z" fill="var(--brand-blue)"/></svg>
        0452918730
      </li>
      <li>
        <svg viewBox="0 0 12 12"><rect x="0.5" y="2" width="11" height="8" fill="var(--brand-blue)"/><path d="M0.5 2 L6 7 L11.5 2" stroke="#fff" fill="none" stroke-width="1"/></svg>
        Info@KPTBuilding.example.au
      </li>
      <li>
        <svg viewBox="0 0 12 12"><circle cx="6" cy="6" r="5.5" fill="var(--brand-blue)"/><path d="M0.5 6 H11.5 M6 0.5 Q2.5 6 6 11.5 M6 0.5 Q9.5 6 6 11.5" stroke="#fff" fill="none" stroke-width="0.8"/></svg>
        www.KPTBuilding.example.au
      </li>
    </ul>

    <p class="licence">Licence Number 871406D</p>
  </section>

  <section class="card card--back" aria-label="Business card back">
    <div class="brand-name"><span class="brand-name__mark"></span>KPT Building</div>
  </section>
</main>
</body>
</html>
```